Redesign existing website.

I need a holidayhouse webdisain. Please review existing website: www.sorvimaja.ee
I want to keep my logo.
Target Market(s)
Nature and sea enjoying holidaymakers, aged 30 to 70
Requirements
Must have
- 3 languages (English, Russian and Estonian)

```html
<!DOCTYPE html>
<html lang="et">
<head>
<meta charset="utf-8">
<title>Sorvi Puhkemaja – Hinnakiri</title>
<link rel="stylesheet" href="https://fonts.googleapis.com/css2?family=Open+Sans:wght@400;600;700&family=Signika:wght@500;600&family=Nunito+Sans:wght@400;600&family=PT+Serif:ital@1&display=swap">
<style>
:root{
  --sky-top:#1659c8;
  --sky-low:#6f9fd6;
  --photo-tone:#8ea6b6;
  --nav-bg:#f3f3f3;
  --accent-yellow:#fff36b;
  --yellow-border:#e2c61a;
  --brown:#8a3a17;
  --alert-red:#e8210f;
  --table-green:#009372;
  --table-green-dark:#007e61;
  --row-a:#e3e3e5;
  --row-b:#f1f1f3;
  --text:#222;
  --footer:#3a3a3a;
  --white:#fff;
}
*{margin:0;padding:0;box-sizing:border-box}
html,body{width:1200px;height:1022px;overflow:hidden;background:var(--white)}
body{position:relative;font-family:"Nunito Sans",Arial,sans-serif;color:var(--text)}
.hero-backdrop{position:absolute;left:0;top:0;width:1200px;height:600px;
  background:linear-gradient(to bottom,var(--sky-top) 0%,var(--sky-low) 55%,var(--white) 97%);}
.brand{position:absolute;left:232px;top:30px;display:flex;align-items:center;gap:18px}
.brand-mark{width:72px;height:72px;border-radius:50%;background:var(--white)}
.brand-name{font-family:"Open Sans",sans-serif;font-weight:700;font-size:24px;line-height:28px;color:var(--white);letter-spacing:.5px}
.languages{position:absolute;right:228px;top:25px;display:flex;gap:7px}
.languages svg{display:block}
.contact{position:absolute;right:228px;top:76px;text-align:right;font-family:"Open Sans",sans-serif;font-size:14px;line-height:21px;color:var(--white)}
.contact div{display:flex;align-items:center;justify-content:flex-end;gap:8px}
.main-nav{position:absolute;left:228px;top:133px;width:744px;height:38px;background:var(--nav-bg);box-shadow:0 4px 6px rgba(0,0,0,.25);display:flex;padding-left:48px}
.main-nav a{font-family:"Open Sans",sans-serif;font-weight:600;font-size:13px;color:#333;text-decoration:none;height:38px;line-height:38px;text-align:center}
.main-nav a:nth-child(1){width:117px}
.main-nav a:nth-child(2){width:112px}
.main-nav a:nth-child(3){width:106px}
.main-nav a:nth-child(4){width:96px}
.main-nav a:nth-child(5){width:111px}
.main-nav a:nth-child(6){width:107px}
.main-nav a.is-active{background:var(--accent-yellow)}
.house-photo{position:absolute;left:400px;top:203px;width:490px;height:300px;background:var(--white);padding:12px;transform:rotate(1.8deg);box-shadow:2px 4px 8px rgba(0,0,0,.35)}
.house-photo div{width:100%;height:100%;background:var(--photo-tone)}
.intro-box{position:absolute;left:228px;top:334px;width:256px;height:96px;background:var(--accent-yellow);border:2px solid var(--yellow-border);outline:1px solid var(--yellow-border);outline-offset:-5px;padding:13px 10px 0 11px}
.intro-box h1{font-family:"Signika",sans-serif;font-weight:600;font-size:18px;color:var(--brown);line-height:20px}
.intro-box p{font-family:"PT Serif",serif;font-style:italic;font-size:12.6px;line-height:13.5px;color:#333;margin-top:3px;letter-spacing:-.1px}
.season-note{position:absolute;top:547px;width:1200px;text-align:center;font-family:"Signika",sans-serif;font-weight:600;font-size:21px;color:var(--alert-red);letter-spacing:.3px}
.price-table{position:absolute;left:291px;top:587px;width:618px;border-collapse:collapse;font-size:13px}
.price-table th{background:var(--table-green);color:var(--white);font-weight:600;height:61px;line-height:17px;position:relative;border-left:1px solid var(--white)}
.price-table th:first-child{border-left:0}
.price-table th.col-night{background:var(--table-green-dark)}
.price-table th .corner{position:absolute;left:0;top:0;width:0;height:0;border-top:15px solid var(--alert-red);border-right:15px solid transparent}
.price-table th .corner.yellow{border-top-color:var(--accent-yellow)}
.price-table td{height:54px;text-align:center;border-left:1px solid var(--white);border-top:1px solid var(--white)}
.price-table td:first-child{text-align:left;padding-left:17px;border-left:0}
.price-table tr:nth-child(odd) td{background:var(--row-a)}
.price-table tr:nth-child(even) td{background:var(--row-b)}
.info{position:absolute;left:291px;top:831px;width:600px;font-size:13px;line-height:18px}
.info .checkin{color:var(--alert-red)}
.info p+p{margin-top:17px}
.site-footer{position:absolute;left:0;top:971px;width:1200px;height:51px;background:var(--footer);color:var(--white);font-family:Arial,sans-serif;font-size:11px;text-align:center;line-height:52px}
</style>
</head>
<body>
<div class="hero-backdrop" role="img" aria-label="Header photo: sandy beach with pine forest by the open sea under a blue sky"></div>

<header>
  <div class="brand"><span class="brand-mark"></span><span class="brand-name">SORVI<br>PUHKEMAJA</span></div>
  <nav class="languages" aria-label="Language">
    <svg width="28" height="20" viewBox="0 0 28 20" aria-label="English"><rect width="28" height="20" fill="#fff"/><g fill="#c8102e"><rect y="0" width="28" height="2"/><rect y="4" width="28" height="2"/><rect y="8" width="28" height="2"/><rect y="12" width="28" height="2"/><rect y="16" width="28" height="2"/></g><rect width="12" height="10" fill="#1f3a7a"/></svg>
    <svg width="28" height="20" viewBox="0 0 28 20" aria-label="Русский"><rect width="28" height="7" fill="#fff"/><rect y="7" width="28" height="6" fill="#1c4fb8"/><rect y="13" width="28" height="7" fill="#d52b1e"/></svg>
    <svg width="28" height="20" viewBox="0 0 28 20" aria-label="Eesti"><rect width="28" height="7" fill="#0072ce"/><rect y="7" width="28" height="6" fill="#000"/><rect y="13" width="28" height="7" fill="#fff"/></svg>
  </nav>
  <div class="contact">
    <div>+372 55 01 234 <svg width="10" height="15" viewBox="0 0 10 15"><rect x="1" y="1" width="8" height="13" rx="1.5" fill="none" stroke="#f4e13a" stroke-width="1.6"/><rect x="3.5" y="11" width="3" height="1.2" fill="#f4e13a"/></svg></div>
    <div>info@sorvimaja.ee <svg width="13" height="10" viewBox="0 0 13 10"><rect width="13" height="10" fill="#f4e13a"/><path d="M0 0l6.5 5.5L13 0" fill="none" stroke="#2f6fc0" stroke-width="1.2"/></svg></div>
  </div>
  <nav class="main-nav">
    <a href="#">TUTVUSTUS</a><a href="#" class="is-active">HINNAKIRI</a><a href="#">ASUKOHT</a><a href="#">GALERII</a><a href="#">HUVITAVAT</a><a href="#">KONTAKT</a>
  </nav>
</header>

<main>
  <figure class="house-photo"><div role="img" aria-label="Photo of the holiday house with a red tiled roof, white balcony, stone walls and a terrace"></div></figure>
  <section class="intro-box">
    <h1>MEIE HINNAKIRI</h1>
    <p>Lorem ipsum dolor sit amet, consectetur<br>adipiscing elit. Ut sit amet metus ut<br>lorem pharetra venenatis fermentum at</p>
  </section>

  <h2 class="season-note">DETS, JAAN, VEEBR, MÄRTS - PUHKEMAJA SULETUD</h2>

  <table class="price-table">
    <thead>
      <tr>
        <th style="width:202px"></th>
        <th class="col-night" style="width:86px"><span class="corner"></span>Ööpäev<br>(1 night)</th>
        <th style="width:86px"><span class="corner yellow"></span>1 nädal<br>(1 week)</th>
        <th style="width:140px"><span class="corner"></span>Nädalavahetus<br>Weekend Fr - Sun</th>
        <th><span class="corner yellow"></span>Ööbimine<br>paadis</th>
      </tr>
    </thead>
    <tbody>
      <tr><td>mai, oktoober</td><td>75 EUR</td><td>405 EUR</td><td>200 EUR</td><td>-</td></tr>
      <tr><td>juuni, juuli, august, sept</td><td>95 EUR</td><td>450 EUR</td><td>215 EUR</td><td>20 EUR</td></tr>
      <tr><td>Rannamaja</td><td>90 EUR</td><td>450 EUR</td><td>200 EUR</td><td>-</td></tr>
    </tbody>
  </table>

  <div class="info">
    <p class="checkin">Sisseregistreerimine, check in 15:00-18:00<br>Maja vabastatakse, check out 12:00</p>
    <p>Broneeringu annuleerimisel vähemalt nädal enne saabumispäeva tagastame ettemaksust 50%. Hilisema<br>annuleerimise või külalise mitteilmumise korral ettemaksu ei tagastata.</p>
    <p>Sorvi Puhkemaja siseruumides ei suitsetata.</p>
  </div>
</main>

<footer class="site-footer">Copyright © 2014 www.sorvimaja.ee. All Rights Reserved.</footer>
</body>
</html>
```